Need a business card for our overland brand!

We had the logo made and we need a great design for our business card. Use the logo provide or tweak it however you see fit.

Contact Information for Business Card

Name, Title, Telephone, email, website

```html
<!DOCTYPE html>
<html lang="en">
<head>
<meta charset="utf-8">
<title>Fjord Traverse — Business Card</title>
<link rel="stylesheet" href="https://fonts.googleapis.com/css2?family=Montserrat:wght@400;500;700&display=swap">
<style>
  :root {
    --navy: #253a56;
    --navy-deep: #1f3350;
    --teal: #21a3c6;
    --white: #ffffff;
    --ink: #222222;
    --backdrop: #3a3a3c;
  }
  * { box-sizing: border-box; margin: 0; padding: 0; }
  html, body {
    width: 1200px; height: 1200px; overflow: hidden;
    background: var(--backdrop);
    font-family: "Montserrat", sans-serif;
  }
  .sheet {
    width: 1200px; height: 1200px;
    display: flex; flex-direction: column; align-items: center; justify-content: center;
    gap: 60px;
  }
  .card {
    position: relative;
    width: 900px; height: 514px;
    border-radius: 34px;
    overflow: hidden;
  }

  /* Front */
  .card-front { background: var(--white); }
  .front-notch {
    position: absolute; left: 0; top: 232px;
    width: 0; height: 0;
    border-top: 26px solid transparent;
    border-bottom: 26px solid transparent;
    border-left: 30px solid var(--teal);
  }
  .contact {
    position: absolute; left: 96px; top: 222px;
  }
  .contact-name {
    color: var(--teal); font-weight: 500;
    font-size: 46px; letter-spacing: 1px; line-height: 1;
  }
  .contact-position {
    color: var(--ink); font-weight: 400;
    font-size: 22px; letter-spacing: 1.5px; margin-top: 4px;
  }
  .contact-list { list-style: none; margin-top: 22px; }
  .contact-list li {
    display: flex; align-items: center; gap: 16px;
    color: var(--ink); font-size: 23px; letter-spacing: 0.5px;
    height: 40px;
  }
  .contact-list svg { width: 26px; height: 26px; flex: none; fill: var(--teal); }
  .front-brand {
    position: absolute; right: 90px; top: 120px;
    text-align: center;
    color: var(--navy); font-weight: 700;
    font-size: 64px; line-height: 0.95; letter-spacing: 1px;
  }
  .band-teal {
    position: absolute; left: 0; bottom: 0;
    width: 590px; height: 28px; background: var(--teal);
  }
  .band-navy {
    position: absolute; right: 0; bottom: 0;
    width: 300px; height: 34px; background: var(--navy);
  }

  /* Back */
  .card-back {
    background: radial-gradient(circle at 70% 20%, #2f4764 0%, var(--navy) 45%, var(--navy-deep) 100%);
    border-bottom: 4px solid var(--teal);
    display: flex; align-items: center; justify-content: center;
  }
  .back-brand {
    display: flex; align-items: center; gap: 28px;
  }
  .back-mark {
    width: 40px; height: 40px; border-radius: 50%; background: var(--teal);
  }
  .back-name {
    color: var(--white); font-weight: 700;
    font-size: 88px; line-height: 0.95; letter-spacing: 1px;
  }
</style>
</head>
<body>
<main class="sheet">

  <section class="card card-front" aria-label="Business card front">
    <span class="front-notch"></span>
    <div class="contact">
      <h1 class="contact-name">FULL NAME</h1>
      <p class="contact-position">POSITION</p>
      <ul class="contact-list">
        <li>
          <svg viewBox="0 0 24 24" aria-hidden="true"><path d="M6.6 10.8a15.1 15.1 0 0 0 6.6 6.6l2.2-2.2a1 1 0 0 1 1-.25 11.4 11.4 0 0 0 3.6.57 1 1 0 0 1 1 1V20a1 1 0 0 1-1 1A17 17 0 0 1 3 4a1 1 0 0 1 1-1h3.5a1 1 0 0 1 1 1c0 1.25.2 2.45.57 3.57a1 1 0 0 1-.25 1z"/></svg>
          (000) 000 0000
        </li>
        <li>
          <svg viewBox="0 0 24 24" aria-hidden="true"><path d="M2 5h20v14H2z M3.5 6.5l8.5 6.5 8.5-6.5v-.1H3.5z" fill-rule="evenodd"/></svg>
          email@company.com
        </li>
        <li>
          <svg viewBox="0 0 24 24" aria-hidden="true"><path d="M12 2a10 10 0 1 0 0 20 10 10 0 0 0 0-20zm0 1.8c1 0 2.2 1.8 2.8 5.2H9.2C9.8 5.6 11 3.8 12 3.8zM8.9 11h6.2a20 20 0 0 1 0 2H8.9a20 20 0 0 1 0-2zm-1.9 0a22 22 0 0 0 0 2H3.9a8 8 0 0 1 0-2zm10 0h3.1a8 8 0 0 1 0 2H17a22 22 0 0 0 0-2zM9.2 15h5.6c-.6 3.4-1.8 5.2-2.8 5.2S9.8 18.4 9.2 15zM4.6 9a8.2 8.2 0 0 1 4.3-4.5A14 14 0 0 0 7.4 9zm12 0a14 14 0 0 0-1.5-4.5A8.2 8.2 0 0 1 19.4 9zM4.6 15h2.8a14 14 0 0 0 1.5 4.5A8.2 8.2 0 0 1 4.6 15zm12 0h2.8a8.2 8.2 0 0 1-4.3 4.5 14 14 0 0 0 1.5-4.5z"/></svg>
          www.company.com
        </li>
      </ul>
    </div>
    <div class="front-brand">FJORD<br>TRAVERSE</div>
    <span class="band-teal"></span>
    <span class="band-navy"></span>
  </section>

  <section class="card card-back" aria-label="Business card back">
    <div class="back-brand">
      <span class="back-mark"></span>
      <div class="back-name">FJORD<br>TRAVERSE</div>
    </div>
  </section>

</main>
</body>
</html>
```